Mobil Battery Sales and Instalation

We are a automotive roadside svc company. I am looking to focus on battery sales and instalation We offer tire changes, lockuot, jump starts fuel delivry and battery sales This design should be battery sales and instalation focused My company name is. Harbor Lane Svcs. 909-512-7364 call or text Hours 7am to 9pm. Free service call and instalation with purchase of new battery. Free testing Free battery disposal Colors we like are black and orange or red and black

Target Market(s)

Automotive, RV, Comerical truck, motorcycle and boat

Industry/Entity Type

Automotive

Requirements
Must have
• Pic of battery
• Mobil battery service.
Nice to have
• I want people to see this card and know its a mobil service for battery sales and installation. But can see we offer other services.
• Use my company name but i dont want that to be the standout. (Tuck it in somewhere).
Should not have
• No pictures of any trucks cars etc.
• we do not tow!

```html
<!DOCTYPE html>
<html lang="en">
<head>
<meta charset="utf-8">
<title>Harbor Lane Svcs – Mobile Battery Postcard</title>
<link href="https://fonts.googleapis.com/css2?family=Archivo+Black&family=Oswald:wght@400;600;700&display=swap" rel="stylesheet">
<style>
  :root {
    --canvas-bg: #ecebe8;
    --ink: #111111;
    --header-black: #1a1a1a;
    --orange: #f26522;
    --orange-deep: #e8541a;
    --yellow: #ffd21f;
    --amber: #f7a81b;
    --white: #ffffff;
    --grey-light: #e6e6e6;
    --grey-mid: #c9c9c9;
    --photo-engine-a: #3a3f47;
    --photo-engine-b: #8a8f96;
    --photo-battery-a: #1d4f9c;
    --photo-battery-b: #7fb3e8;
  }
  * { box-sizing: border-box; margin: 0; padding: 0; }
  html, body {
    width: 1200px; height: 444px; overflow: hidden;
    background: var(--canvas-bg);
  }
  .stage { position: relative; width: 1200px; height: 444px; }

  /* ---------- Front card ---------- */
  .card-front {
    position: absolute; left: 42px; top: 42px; width: 565px; height: 368px;
    background: var(--header-black); overflow: hidden;
    font-family: "Archivo Black", "Arial Black", sans-serif;
  }
  .headline {
    position: absolute; left: 0; top: 14px; width: 100%;
    text-align: center; color: var(--yellow); font-size: 24px; line-height: 31px; font-weight: normal;
  }
  .headline .free { color: var(--orange); font-size: 29px; }

  .photo-engine {
    position: absolute; left: 0; top: 86px; width: 290px; height: 170px;
    background: linear-gradient(135deg, var(--photo-engine-a), var(--photo-engine-b) 55%, var(--photo-engine-a));
  }
  .photo-batteries {
    position: absolute; left: 0; top: 256px; width: 300px; height: 112px;
    background: linear-gradient(180deg, var(--photo-battery-b), var(--photo-battery-a));
  }

  .offer-area { position: absolute; left: 0; top: 0; width: 565px; height: 368px; }

  .contact-panel {
    position: absolute; left: 288px; top: 86px; width: 277px; height: 87px;
    background: var(--white); text-align: center; color: var(--ink);
  }
  .contact-panel .phone {
    display: flex; align-items: center; justify-content: center; gap: 6px;
    margin-top: 7px; color: var(--orange-deep); font-size: 27px; line-height: 30px;
  }
  .contact-panel .phone svg { width: 26px; height: 26px; }
  .contact-panel .line { font-size: 18px; line-height: 21px; }

  .perks {
    position: absolute; left: 288px; top: 173px; width: 277px; height: 62px;
    background: var(--header-black); color: var(--yellow);
    font-family: "Oswald", "Arial Narrow", sans-serif; font-weight: 700;
    font-size: 22px; line-height: 26px; padding: 5px 0 0 10px; white-space: nowrap;
  }
  .perks li { list-style: none; }
  .perks .tick { margin-right: 5px; }

  .offer-list {
    position: absolute; left: 338px; top: 246px; color: var(--ink);
    font-size: 14px; line-height: 17px;
  }
  .offer-list h3 { font-size: 14px; font-weight: normal; margin-bottom: 2px; }
  .offer-list li { list-style: none; margin-left: 4px; }
  .offer-list li::before { content: "• "; }

  .company-pill {
    position: absolute; left: 37px; top: 242px; width: 223px; height: 26px;
    background: var(--orange-deep); border-radius: 13px; border: 2px solid var(--header-black);
    color: var(--ink); font-size: 15px; line-height: 22px; text-align: center;
  }

  /* ---------- Back card ---------- */
  .card-back {
    position: absolute; left: 617px; top: 42px; width: 545px; height: 368px;
    background: linear-gradient(90deg, var(--grey-light), var(--white) 45%, var(--white));
    overflow: hidden; font-family: "Oswald", "Arial Narrow", sans-serif;
  }
  .stripe-top {
    position: absolute; left: 0; top: 14px; width: 100%; height: 14px;
    background: linear-gradient(90deg, var(--white), var(--grey-mid) 30%, var(--amber) 70%, var(--orange));
  }
  .stripe-bottom {
    position: absolute; left: 0; top: 338px; width: 100%; height: 14px;
    background: linear-gradient(90deg, var(--white), var(--grey-mid) 35%, var(--ink));
  }
  .stamp-box {
    position: absolute; left: 467px; top: 38px; width: 56px; height: 58px;
    border: 2px dashed var(--grey-mid);
  }
  .back-copy {
    position: absolute; left: 12px; top: 44px; width: 270px; text-align: center; color: var(--ink);
  }
  .back-copy .free { color: var(--orange); font-size: 40px; font-weight: 700; line-height: 46px; }
  .back-copy .offer { font-size: 23px; font-weight: 600; line-height: 26px; }
  .back-copy .battery { color: var(--orange); font-size: 23px; font-weight: 700; line-height: 27px; }
  .back-copy .value { font-size: 19px; font-weight: 400; line-height: 25px; }
  .back-copy .phone {
    display: flex; align-items: center; justify-content: center; gap: 6px;
    margin-top: 16px; color: var(--orange-deep);
    font-family: "Archivo Black", "Arial Black", sans-serif; font-size: 26px; line-height: 32px;
  }
  .back-copy .phone svg { width: 24px; height: 24px; }
  .back-copy .line {
    font-family: "Archivo Black", "Arial Black", sans-serif; font-size: 17px; line-height: 22px;
  }
</style>
</head>
<body>
<main class="stage">

  <section class="card-front">
    <h1 class="headline"><span class="free">FREE</span> service call and instalation<br>with purchase of new battery</h1>

    <div class="photo-engine" role="img" aria-label="Technician lifting a car battery out of an engine bay"></div>
    <div class="photo-batteries" role="img" aria-label="Row of three new car batteries on a blue background"></div>

    <svg class="offer-area" viewBox="0 0 565 368" aria-hidden="true">
      <defs>
        <linearGradient id="offerFill" x1="0" y1="0" x2="0" y2="1">
          <stop offset="0" stop-color="#ffd21f"/>
          <stop offset="1" stop-color="#f7941d"/>
        </linearGradient>
      </defs>
      <path d="M300 235 L565 235 L565 368 L278 368 Q262 300 300 235 Z" fill="url(#offerFill)"/>
      <path d="M300 235 Q262 300 278 368" fill="none" stroke="#f26522" stroke-width="5"/>
    </svg>

    <div class="contact-panel">
      <p class="phone">
        <svg viewBox="0 0 26 26" aria-hidden="true">
          <circle cx="13" cy="13" r="11.5" fill="none" stroke="#e8541a" stroke-width="2"/>
          <path d="M9 7 l3 0 l1 4 l-2 1 q1 3 4 4 l1-2 l4 1 l0 3 q-8 1-11-11 z" fill="#e8541a"/>
        </svg>
        909.512.7364
      </p>
      <p class="line">Call or text</p>
      <p class="line">Hours 7AM to 9PM</p>
    </div>

    <ul class="perks">
      <li><span class="tick">✔</span>FREE TESTING</li>
      <li><span class="tick">✔</span>FREE BATTERY DISPOSAL</li>
    </ul>

    <div class="offer-list">
      <h3>WE OFFER</h3>
      <ul>
        <li>Tire Changes</li>
        <li>Lockuot</li>
        <li>Jump Starts</li>
        <li>Fuel Delivery</li>
        <li>Battery Sales</li>
      </ul>
    </div>

    <p class="company-pill">Harbor Lane Svcs</p>
  </section>

  <section class="card-back">
    <div class="stripe-top"></div>
    <div class="stamp-box"></div>
    <div class="back-copy">
      <p class="free">FREE</p>
      <p class="offer">service call &amp; installation<br>with purchase of</p>
      <p class="battery">NEW BATTERY</p>
      <p class="value">($9.99 value)</p>
      <p class="phone">
        <svg viewBox="0 0 26 26" aria-hidden="true">
          <circle cx="13" cy="13" r="11.5" fill="none" stroke="#e8541a" stroke-width="2"/>
          <path d="M9 7 l3 0 l1 4 l-2 1 q1 3 4 4 l1-2 l4 1 l0 3 q-8 1-11-11 z" fill="#e8541a"/>
        </svg>
        909.512.7364
      </p>
      <p class="line">Call or text</p>
      <p class="line">Hours 7AM to 9PM</p>
    </div>
    <div class="stripe-bottom"></div>
  </section>

</main>
</body>
</html>
```